Harbor Fieldworks (Business Card Design)

Need business cards designed. Something modern, chic, and sleek. Mabye the back of the card should be the navy blue that is in the logo and then just the logo on the back.

Target Market(s)

Those in the hotel, office, and renovation industry

Contact Information for Business Card

1. Logo 2. Dorian Velasko 3. CEO/Founder 4. Phone: (833) HarbFld / (833) 427-2353 5. Email: dorian@theharborfieldworks.com 6. Website: www.theharborfieldworks.com

Font styles to use
Other font styles liked:
• Look at the logo font and base the font for everything else off of that.

Colors
0054AA
0677BA
7BADD7
CADEEF
E8F1F8

Requirements
Must have
• Colors that are associated in the logo
Nice to have
• Sleek modern clean and chic design.

```html
<!DOCTYPE html>
<html lang="en">
<head>
<meta charset="utf-8">
<title>Harbor Fieldworks — Business Card</title>
<link href="https://fonts.googleapis.com/css2?family=Montserrat:wght@400;500;600&display=swap" rel="stylesheet">
<style>
  :root {
    --navy: #0b1846;
    --gold: #cfa247;
    --white: #ffffff;
    --ink-soft: #e9ecf5;
    --divider: rgba(255,255,255,0.28);
    --backdrop: #3d3d3f;
  }
  * { box-sizing: border-box; margin: 0; padding: 0; }
  html, body {
    width: 1200px; height: 1200px; overflow: hidden;
    background: var(--backdrop);
    font-family: "Montserrat", sans-serif;
  }
  .sheet {
    width: 1200px; height: 1200px;
    display: flex; flex-direction: column; align-items: center; justify-content: center;
    gap: 60px;
  }
  .card {
    width: 900px; height: 514px;
    border-radius: 38px;
    overflow: hidden;
    position: relative;
  }
  /* Front */
  .card--front { background: var(--white); }
  .front__brand {
    position: absolute; left: 0; right: 0; top: 0; height: 270px;
    display: flex; align-items: center; justify-content: center; gap: 16px;
  }
  .brand-mark { width: 16px; height: 16px; background: var(--gold); }
  .brand-name {
    font-weight: 500; letter-spacing: 0.14em; text-transform: uppercase;
    font-size: 38px; color: var(--navy);
  }
  .front__rule {
    position: absolute; left: 0; right: 0; top: 276px; height: 8px;
    background: var(--gold);
  }
  .front__band {
    position: absolute; left: 0; right: 0; top: 294px; bottom: 0;
    background: var(--navy);
    display: flex; align-items: center;
  }
  .person { width: 400px; padding-left: 70px; }
  .person__name {
    color: var(--gold); font-weight: 600; font-size: 30px; letter-spacing: 0.01em;
    text-transform: uppercase;
  }
  .person__title { color: var(--white); font-size: 20px; margin-top: 6px; }
  .band__divider { width: 1px; height: 140px; background: var(--divider); }
  .contact { list-style: none; padding-left: 46px; }
  .contact__item {
    display: flex; align-items: center; gap: 14px;
    color: var(--ink-soft); font-size: 18px; line-height: 1; margin: 13px 0;
  }
  .contact__icon { width: 20px; height: 20px; flex: none; }
  /* Back */
  .card--back {
    background: var(--navy);
    display: flex; align-items: center; justify-content: center; gap: 20px;
  }
  .card--back .brand-name { color: var(--white); font-size: 50px; }
  .card--back .brand-mark { width: 20px; height: 20px; }
</style>
</head>
<body>
<main class="sheet">
  <section class="card card--front" aria-label="Business card front">
    <div class="front__brand">
      <span class="brand-name">Harbor Fieldworks</span>
      <span class="brand-mark"></span>
    </div>
    <div class="front__rule"></div>
    <div class="front__band">
      <div class="person">
        <p class="person__name">Dorian Velasko</p>
        <p class="person__title">CEO | FOUNDER</p>
      </div>
      <div class="band__divider"></div>
      <ul class="contact">
        <li class="contact__item">
          <svg class="contact__icon" viewBox="0 0 24 24" fill="var(--gold)"><path d="M6.6 10.8a15.1 15.1 0 0 0 6.6 6.6l2.2-2.2a1 1 0 0 1 1-.25 11.4 11.4 0 0 0 3.6.6 1 1 0 0 1 1 1V20a1 1 0 0 1-1 1A17 17 0 0 1 3 4a1 1 0 0 1 1-1h3.5a1 1 0 0 1 1 1c0 1.25.2 2.45.6 3.6a1 1 0 0 1-.25 1z"/></svg>
          <span>(833) HarbFld | (833) 427-2353</span>
        </li>
        <li class="contact__item">
          <svg class="contact__icon" viewBox="0 0 24 24" fill="var(--gold)"><path d="M2 5h20v14H2z" fill="none" stroke="var(--gold)" stroke-width="2"/><path d="M2 5l10 8 10-8" fill="none" stroke="var(--gold)" stroke-width="2"/></svg>
          <span>dorian@theharborfieldworks.com</span>
        </li>
        <li class="contact__item">
          <svg class="contact__icon" viewBox="0 0 24 24" fill="none" stroke="var(--gold)" stroke-width="1.8"><circle cx="12" cy="12" r="10"/><ellipse cx="12" cy="12" rx="4.5" ry="10"/><path d="M2 12h20M4 7h16M4 17h16"/></svg>
          <span>www.theharborfieldworks.com</span>
        </li>
      </ul>
    </div>
  </section>

  <section class="card card--back" aria-label="Business card back">
    <span class="brand-name">Harbor Fieldworks</span>
    <span class="brand-mark"></span>
  </section>
</main>
</body>
</html>
```